Original business card of a small accounting firm

My firm specializes in accounting and taxes for small businesses. I'm looking for an original and creative business card as a marketing tool to give to prospective clients; however since we are a professional firm the card must also appear professional. I'm uploading a few examples of what I believe may fit my needs. Please feel free to use them as a jumping off point. Lastly, I'm uploading the company logo which I'd like to be the focal point on the back of the card and somewhat incorporated on the front on a smaller scale. I hope my description was helpful.
Target Market(s)
Tax clients and small businesses
Industry/Entity Type
Accounting
Contact Information for Business Card
Gerald Whitcombe
Certified Public Accountant │President
Whitcombe Advisors
T│ (555) 417-2863
Email│GWhitcombe@WhitcombeAdvisors.example
Look and feel
Each slider illustrates characteristics of the customer's brand and the style your logo design should communicate.

```html
<!DOCTYPE html>
<html lang="en">
<head>
<meta charset="utf-8">
<title>Whitcombe Advisors – Business Card</title>
<link href="https://fonts.googleapis.com/css2?family=Lato:ital,wght@0,400;0,700;1,400&display=swap" rel="stylesheet">
<style>
  :root {
    --paper: #ffffff;
    --ink-grey: #595959;
    --ink-dark: #4a4a4a;
    --brand-blue: #2b5ba8;
    --icon-blue: #2a5aa6;
    --wash-blue: #8fb4df;
    --wash-violet: #8a8cc4;
  }
  html, body {
    margin: 0;
    padding: 0;
    width: 1200px;
    height: 702px;
    overflow: hidden;
    background: var(--paper);
  }
  .card {
    position: relative;
    width: 1200px;
    height: 702px;
    background: var(--paper);
    font-family: "Lato", Arial, sans-serif;
    overflow: hidden;
  }

  /* Brand block, top left */
  .brand {
    position: absolute;
    left: 66px;
    top: 118px;
    width: 310px;
    text-align: center;
  }
  .brand__row {
    display: flex;
    align-items: center;
    justify-content: center;
    gap: 10px;
  }
  .brand__mark {
    width: 22px;
    height: 22px;
    background: var(--brand-blue);
  }
  .brand__name {
    font-size: 28px;
    font-weight: 700;
    color: var(--ink-dark);
    letter-spacing: 0.2px;
    white-space: nowrap;
  }
  .brand__tagline {
    margin-top: 6px;
    font-size: 11.5px;
    letter-spacing: 2.1px;
    text-transform: uppercase;
    color: var(--ink-dark);
    white-space: nowrap;
  }

  /* Soft decorative wash, lower left */
  .wash {
    position: absolute;
    left: -40px;
    top: 280px;
    width: 620px;
    height: 460px;
    background:
      radial-gradient(ellipse 60% 55% at 35% 45%, rgba(143,180,223,0.55), rgba(143,180,223,0) 70%),
      radial-gradient(ellipse 45% 40% at 70% 40%, rgba(138,140,196,0.45), rgba(138,140,196,0) 70%),
      radial-gradient(ellipse 30% 35% at 5% 20%, rgba(150,150,150,0.35), rgba(150,150,150,0) 70%);
  }

  /* Contact block, right */
  .contact {
    position: absolute;
    left: 680px;
    width: 492px;
    top: 140px;
    text-align: center;
    color: var(--ink-grey);
  }
  .contact__name {
    margin: 0;
    font-size: 48px;
    font-weight: 700;
    line-height: 1;
    color: var(--ink-grey);
    white-space: nowrap;
  }
  .contact__name .surname { color: var(--brand-blue); }
  .contact__credential {
    margin: 4px 0 0;
    font-size: 20px;
    font-style: italic;
    color: var(--ink-grey);
  }
  .contact__role {
    margin: 18px 0 0;
    font-size: 29px;
    font-weight: 400;
    line-height: 1.02;
    color: var(--ink-grey);
  }
  .contact__role .accent { color: var(--brand-blue); }

  .contact__item {
    display: flex;
    flex-direction: column;
    align-items: center;
  }
  .contact__item--phone { margin-top: 40px; }
  .contact__item--email { margin-top: 36px; }
  .icon-badge {
    width: 58px;
    height: 58px;
    border-radius: 50%;
    background: var(--icon-blue);
    display: flex;
    align-items: center;
    justify-content: center;
  }
  .contact__value {
    margin-top: 14px;
    font-size: 25px;
    font-weight: 700;
    color: var(--ink-grey);
    white-space: nowrap;
  }
  .contact__value--email { font-weight: 400; font-size: 24px; }
  .contact__value .accent { color: var(--brand-blue); }
</style>
</head>
<body>
<div class="card">

  <div class="wash" role="img" aria-label="Faint blue and violet brand pattern"></div>

  <div class="brand">
    <div class="brand__row">
      <span class="brand__mark"></span>
      <span class="brand__name">Whitcombe Advisors</span>
    </div>
    <div class="brand__tagline">Small business accounting and taxes</div>
  </div>

  <div class="contact">
    <h1 class="contact__name">Gerald <span class="surname">Whitcombe</span></h1>
    <p class="contact__credential">Certified Public Accountant</p>
    <p class="contact__role">President<br><span class="accent">Whitcombe</span> Advisors</p>

    <div class="contact__item contact__item--phone">
      <span class="icon-badge">
        <svg width="30" height="30" viewBox="0 0 24 24" aria-hidden="true">
          <path fill="#ffffff" d="M6.6 10.8c1.4 2.8 3.8 5.1 6.6 6.6l2.2-2.2c.3-.3.7-.4 1-.2 1.1.4 2.3.6 3.6.6.6 0 1 .4 1 1V20c0 .6-.4 1-1 1C10.6 21 3 13.4 3 4c0-.6.4-1 1-1h3.5c.6 0 1 .4 1 1 0 1.3.2 2.5.6 3.6.1.3 0 .7-.2 1L6.6 10.8z"/>
        </svg>
      </span>
      <span class="contact__value">(555) 417-2863</span>
    </div>

    <div class="contact__item contact__item--email">
      <span class="icon-badge">
        <svg width="30" height="30" viewBox="0 0 24 24" aria-hidden="true">
          <rect x="3" y="6" width="18" height="12" rx="1" fill="#ffffff"/>
          <path d="M3.5 6.5 12 13l8.5-6.5M3.5 17.5l6.3-6M20.5 17.5l-6.3-6" fill="none" stroke="#2a5aa6" stroke-width="1.3"/>
        </svg>
      </span>
      <span class="contact__value contact__value--email"><span class="accent">GWhitcombe</span>@WhitcombeAdvisors.example</span>
    </div>
  </div>

</div>
</body>
</html>
```